Salon Signage

We need a new company sign designed for the exterior of our salon. I have attached our current logos for an idea. I have also attached a photo of what salon looks like currently.

```html
<!DOCTYPE html>
<html lang="en">
<head>
<meta charset="utf-8">
<title>Glosswave Beauty Salon – Exterior Sign</title>
<link rel="stylesheet" href="https://fonts.googleapis.com/css2?family=Archivo+Black&display=swap">
<style>
  :root {
    --backdrop: #ecedec;
    --magenta: #a4288c;
    --hot-pink: #d90f78;
    --ink: #231f20;
    --white: #ffffff;
    --blonde-light: #efe6bf;
    --blonde-mid: #d8c993;
    --blonde-deep: #bfae78;
    --portrait-glow: #f6dfe2;
    --portrait-shade: #e7bcc4;
  }
  * { margin: 0; padding: 0; box-sizing: border-box; }
  html, body {
    width: 1200px;
    height: 514px;
    overflow: hidden;
    background: var(--backdrop);
  }
  .sign {
    position: absolute;
    left: 20px;
    top: 130px;
    width: 1160px;
    height: 254px;
    overflow: hidden;
  }
  .sign-art {
    position: absolute;
    inset: 0;
    width: 1160px;
    height: 254px;
  }
  .brand {
    position: absolute;
    left: 150px;
    top: 22px;
    font-family: "Archivo Black", sans-serif;
    font-weight: 400;
    color: var(--ink);
    line-height: 1;
  }
  .brand-name {
    font-size: 64px;
    letter-spacing: -1px;
  }
  .brand-tagline {
    display: block;
    margin-top: 14px;
    margin-left: 170px;
    font-size: 26px;
    letter-spacing: 0.5px;
  }
</style>
</head>
<body>
  <div class="sign">
    <svg class="sign-art" viewBox="0 0 1160 254" xmlns="http://www.w3.org/2000/svg">
      <defs>
        <linearGradient id="hair-tone" x1="0" y1="0" x2="1" y2="1">
          <stop offset="0" stop-color="var(--blonde-mid)"/>
          <stop offset="0.45" stop-color="var(--blonde-light)"/>
          <stop offset="1" stop-color="var(--blonde-deep)"/>
        </linearGradient>
        <radialGradient id="portrait-tone" cx="0.5" cy="0.45" r="0.6">
          <stop offset="0" stop-color="var(--portrait-glow)"/>
          <stop offset="1" stop-color="var(--portrait-shade)"/>
        </radialGradient>
      </defs>

      <rect class="hair-backdrop" role="img" aria-label="Close-up photograph of flowing blonde hair" x="0" y="0" width="1160" height="254" fill="url(#hair-tone)"/>

      <path class="swoosh-magenta" d="M597,0 C720,20 820,205 960,214 L1160,220 L1160,0 Z" fill="var(--magenta)"/>
      <path class="swoosh-dark" d="M749,0 L1080,0 L1080,212 C960,210 830,150 749,0 Z" fill="var(--ink)"/>
      <path class="swoosh-dark-edge" d="M749,0 C830,150 960,210 1080,212" fill="none" stroke="var(--white)" stroke-width="4"/>

      <circle class="portrait-frame" cx="1042" cy="107" r="118" fill="var(--white)"/>
      <circle class="portrait" role="img" aria-label="Illustrated stylist surrounded by hair dryer, brushes, scissors and colour swatches" cx="1042" cy="107" r="114" fill="url(#portrait-tone)"/>

      <path class="band-pink" d="M0,196 C300,190 700,202 980,214 L1160,222 L1160,254 L0,254 Z" fill="var(--hot-pink)"/>
      <path class="band-pink-tail" d="M960,214 L1160,220 L1160,254 L1100,254 Z" fill="var(--magenta)"/>
      <path class="band-divider" d="M0,216 C400,212 800,224 1150,248" fill="none" stroke="var(--white)" stroke-width="5"/>
      <path class="band-dark" d="M0,221 C400,217 800,229 1120,254 L0,254 Z" fill="var(--ink)"/>

      <circle class="brand-mark" cx="92" cy="96" r="42" fill="var(--magenta)"/>
    </svg>

    <div class="brand">
      <span class="brand-name">GLOSSWAVE</span>
      <span class="brand-tagline">Beauty Salon</span>
    </div>
  </div>
</body>
</html>
```